Motivational Quotes Poster Series

This is a 3 poster design series for Ridgeway Haul Academy. The size of each poster should be 18 inches wide and 24 inches tall. The goal of these posters is to serve as motivational "signs" to be hung in the office area for the employees (not customers). These employees are instructors/teachers, teaching students how to drive semi trucks. While each design is a separate poster and design, we're posting as 1 project because we'd like some continuity between the series. Below we'll break down the details of all 3 posters...

Poster #1
Text that must appear on poster - "If You Want The Best Out Of Each Student" and "Give The Best Of You!" Note: While this text must appear on the poster, you can arrange in the layout as you see fit. For example, first line could be at top of poster and second line on bottom.

Poster #2
Text that must appear on poster - "Invest In People" and "Change Someone's Life" (same notes apply as in 1st poster)

Poster #3
Text that must appear on poster - "Today Is..." and "Just Another Day For You" and "The Most Important Day In Their Life" Note: This can be laid out on the poster however you see fit, but each phrase needs to be separate and it needs to flow.

Target Market(s)

Truck Driver Training Instructors - These are middle-aged, mostly male, masculine type personalities.

Industry/Entity Type

Training

Requirements
Must have
• Must have noted text from description
Must have working files (ie - PSD, EPS, AI, etc) provided
Must have common theme between each poster in series
Must have easy to read font and layout
Must have product dimensions of 18 inches (width) by 24 inches (height). If design uses full dimensions please include quarter inch bleed.
Nice to have
• Nice to have a trucking theme...related to trucking industry, but not over the top. Example - This could mean subtle injection of background tire tracks, but by no means are tire tracks required.

For inspiration, you can visit the site at http://www.ridgewayhaulacademy.com. While you can use the colors of the site/logo, you can still branch out between each poster to try new colors within reason.

Note: While we've attached the logo to this project, it COULD be used but doesn't HAVE to be included in the design. The logo IS NOT a focal point. The phrases in the poster ARE the focal point.

```html
<!DOCTYPE html>
<html lang="en">
<head>
<meta charset="utf-8">
<title>Ridgeway Haul Academy – Motivational Poster Series</title>
<link rel="stylesheet" href="https://fonts.googleapis.com/css2?family=Questrial&display=swap">
<style>
  :root {
    --page: #ffffff;
    --green: #a6c64b;
    --green-ink: #2f5d32;
    --green-ghost: rgba(47, 93, 50, 0.16);
    --blue: #19ade8;
    --blue-ink: #ffffff;
    --blue-ghost: rgba(0, 70, 120, 0.14);
    --red: #b81920;
    --red-ink: #ffffff;
    --red-dark: #111111;
    --red-ghost: rgba(255, 255, 255, 0.13);
  }
  * { box-sizing: border-box; margin: 0; padding: 0; }
  html, body {
    width: 1200px; height: 530px; overflow: hidden;
    background: var(--page);
    font-family: "Questrial", "Century Gothic", sans-serif;
  }
  .series { position: relative; width: 1200px; height: 530px; }
  .poster {
    position: absolute; top: 14px; width: 363px; height: 498px; overflow: hidden;
  }
  .poster--best { left: 17px; background: var(--green); color: var(--green-ink); }
  .poster--people { left: 410px; background: var(--blue); color: var(--blue-ink); }
  .poster--today { left: 803px; background: var(--red); color: var(--red-ink); }

  .ghost-words {
    position: absolute; left: 0; top: 0; width: 100%; height: 100%;
    display: flex; gap: 0; pointer-events: none;
  }
  .ghost-words span {
    writing-mode: vertical-rl; font-size: 92px; line-height: 0.9;
    letter-spacing: -0.02em; white-space: nowrap;
  }
  .poster--best .ghost-words { padding-left: 40px; color: var(--green-ghost); }
  .poster--people .ghost-words { padding-left: 70px; color: var(--blue-ghost); }
  .poster--today .ghost-words { padding-left: 190px; color: var(--red-ghost); }

  .line {
    position: absolute; line-height: 1; white-space: nowrap;
    letter-spacing: -0.015em; text-transform: uppercase;
  }
  .poster--best .line { left: 24px; }
  .poster--people .line { left: 0; width: 100%; text-align: center; }
  .poster--today .line { left: 20px; }
  .line--heavy { -webkit-text-stroke: 1.2px currentColor; }
  .line--dark { color: var(--red-dark); }

  .photo { position: absolute; }
  .photo svg { display: block; width: 100%; height: 100%; }

  .brand {
    position: absolute; bottom: 6px; left: 0; width: 100%;
    display: flex; justify-content: center; align-items: center; gap: 3px;
    font-size: 6px; letter-spacing: 0.02em;
  }
  .brand-dot { width: 6px; height: 6px; border-radius: 50%; background: currentColor; }
</style>
</head>
<body>
<main class="series">

  <section class="poster poster--best">
    <div class="ghost-words" aria-hidden="true"><span>BEST</span><span>BEST</span></div>
    <p class="line" style="top:22px;font-size:45px">If you want</p>
    <p class="line line--heavy" style="top:70px;font-size:56px">The best</p>
    <p class="line" style="top:128px;font-size:45px">Out of each</p>
    <p class="line line--heavy" style="top:175px;font-size:58px">Student</p>
    <div class="photo" style="left:0;top:268px;width:300px;height:92px">
      <svg viewBox="0 0 300 92" role="img" aria-label="Pale green silhouette of a semi truck hauling a trailer along a road">
        <defs><linearGradient id="best-truck" x1="0" y1="0" x2="1" y2="0">
          <stop offset="0" stop-color="#d4e890"/><stop offset="1" stop-color="#c4dd7a"/>
        </linearGradient></defs>
        <line x1="0" y1="80" x2="80" y2="86" stroke="#2f5d32" stroke-width="1.5"/>
        <rect x="70" y="22" width="220" height="64" fill="url(#best-truck)"/>
      </svg>
    </div>
    <p class="line line--heavy" style="top:386px;font-size:56px">Give the</p>
    <p class="line" style="top:446px;font-size:42px">Best of you!</p>
    <div class="brand"><span class="brand-dot"></span><span>Ridgeway Haul Academy</span></div>
  </section>

  <section class="poster poster--people">
    <div class="ghost-words" aria-hidden="true"><span>PEOPLE</span><span>PEOPLE</span><span>PEOPLE</span></div>
    <p class="line" style="top:18px;font-size:84px;letter-spacing:0.02em">Invest</p>
    <p class="line" style="top:108px;font-size:58px">In people</p>
    <div class="photo" style="left:55px;top:190px;width:300px;height:195px">
      <svg viewBox="0 0 300 195" role="img" aria-label="Light blue and white photograph of a semi truck cab with a trailer">
        <defs><linearGradient id="people-truck" x1="0" y1="0" x2="0" y2="1">
          <stop offset="0" stop-color="#e8f6fd"/><stop offset="1" stop-color="#8fd3f3"/>
        </linearGradient></defs>
        <rect x="0" y="0" width="300" height="195" fill="url(#people-truck)"/>
      </svg>
    </div>
    <p class="line" style="top:388px;font-size:70px">Change</p>
    <p class="line" style="top:458px;font-size:37px">Someone’s life</p>
    <div class="brand"><span class="brand-dot"></span><span>Ridgeway Haul Academy</span></div>
  </section>

  <section class="poster poster--today">
    <div class="ghost-words" aria-hidden="true"><span>TODAY</span><span>TODAY</span></div>
    <p class="line line--dark" style="top:20px;font-size:52px">Today is...</p>
    <p class="line" style="top:80px;font-size:41px">Just another</p>
    <p class="line" style="top:130px;font-size:47px">Day for you</p>
    <div class="photo" style="left:18px;top:180px;width:327px;height:158px">
      <svg viewBox="0 0 327 158" role="img" aria-label="Tinted photograph of a semi truck driving between rows of traffic cones on a training course">
        <defs><linearGradient id="today-truck" x1="0" y1="0" x2="0" y2="1">
          <stop offset="0" stop-color="#b81920" stop-opacity="0"/>
          <stop offset="0.45" stop-color="#e8826e"/>
          <stop offset="1" stop-color="#5a0c10"/>
        </linearGradient></defs>
        <rect x="0" y="0" width="327" height="158" fill="url(#today-truck)"/>
      </svg>
    </div>
    <p class="line" style="top:346px;font-size:60px">The most</p>
    <p class="line line--dark" style="top:410px;font-size:46px">Important</p>
    <p class="line" style="top:460px;font-size:32px">Day in their life</p>
    <div class="brand"><span class="brand-dot"></span><span>Ridgeway Haul Academy</span></div>
  </section>

</main>
</body>
</html>
```